Zielgruppe
Massagen und Therapien an Patienten mit Schmerzen an Muskeln und am gesamten Bewegungsapparat. Nachbehandlung nach Operationen und Verletzungen sowie Sportverletzungen therapieren.
Zielgruppe: alle Personen (m/w) jeden alters egal ob sportlich oder 'faul'.
Aufgabenstellung
Das Design soll Ruhe, Harmonie, Vertrautheit und Geborgenheit vermitteln. Es muß mit dem Firmenlogo harmonisieren (Farbe und Gestaltung).
Das Logo und der Text findet sich im Anhang.
Es können Bilder eigenständig hinzugefügt werden.
Unbedingt DIN-Format verwenden (welches bleibt dem Designer überlassen)

```html
<!DOCTYPE html>
<html lang="de">
<head>
<meta charset="utf-8">
<title>Massagepraxis Lindqvorst – Folder</title>
<link href="https://fonts.googleapis.com/css2?family=Questrial&family=Tinos&display=swap" rel="stylesheet">
<style>
:root{
  --blue:#4b7fc3;
  --blue-dark:#3a6aab;
  --green:#8cc63e;
  --green-text:#7cb531;
  --mist:#eef3ec;
  --ink:#3b3b3b;
  --page:#f1f0ed;
  --white:#ffffff;
}
*{box-sizing:border-box;margin:0;padding:0}
html,body{width:1200px;height:667px;overflow:hidden;background:var(--page)}
body{position:relative;font-family:"Questrial",Arial,sans-serif;color:var(--ink)}
.sheet{position:absolute;top:126px;width:585px;height:414px;display:flex;background:var(--white);box-shadow:0 2px 10px rgba(0,0,0,.15)}
.sheet--outside{left:10px}
.sheet--inside{left:605px}
.panel{position:relative;width:195px;height:414px;overflow:hidden}
.panel + .panel{border-left:1px solid #e6e6e6}
.band{position:absolute;left:0;top:0;width:195px;height:50px}
.band-title{position:absolute;left:14px;top:12px;color:var(--white);font-size:10px;font-weight:700;letter-spacing:.1px}
.swoosh{position:absolute;left:0;bottom:0;width:195px;height:72px}
.foot-note{position:absolute;left:14px;right:14px;bottom:14px;color:var(--green-text);font-size:6.5px;line-height:1.4}
.photo{position:absolute;left:0;width:195px}
.copy{position:absolute;left:16px;right:14px;font-size:6.2px;line-height:1.45}
.copy p{margin-bottom:6px}
.copy h4{font-size:6.4px;font-weight:700;margin:4px 0 2px}
.copy ul{list-style:none}
.copy li{padding-left:6px;position:relative}
.copy li::before{content:"";position:absolute;left:0;top:3px;width:3px;height:3px;border-radius:50%;background:var(--blue)}
.hl{color:var(--blue)}
.brand{position:absolute;left:0;right:0;text-align:center}
.brand-dot{display:block;margin:0 auto 6px;border-radius:50%;background:var(--green)}
.brand-name{color:var(--blue);line-height:1.15}
.placeholder{position:absolute;left:58px;top:88px;font-family:"Tinos",serif;font-size:7px;color:#444}
.contact{position:absolute;left:0;right:0;top:290px;text-align:center;font-size:6px;line-height:1.55}
.grid{position:absolute;left:40px;top:152px;width:120px;display:grid;grid-template-columns:repeat(3,38px);gap:3px}
.grid div{height:38px}
.tagline{position:absolute;left:0;right:0;top:320px;text-align:center;color:var(--green-text);font-size:9px}
.cover-note{position:absolute;left:10px;right:10px;bottom:14px;text-align:center;color:var(--blue);font-size:6.8px;line-height:1.4}
.arrow{color:var(--green)}
</style>
</head>
<body>

<!-- Outside of the folder -->
<section class="sheet sheet--outside">
  <article class="panel panel--akupunkt">
    <div class="photo" style="top:40px;height:160px;background:linear-gradient(160deg,#f3e6dc,#e7cfbf 55%,#f6f1ec)" role="img" aria-label="Foto: Akupunkt-Massage im Gesicht einer entspannten Patientin"></div>
    <svg class="band" viewBox="0 0 195 50"><path d="M0 0H195V36Q100 48 0 42Z" fill="var(--blue)"/></svg>
    <h2 class="band-title">Akupunkt-Massage nach Hallbrecht</h2>
    <div class="copy" style="top:218px">
      <p>Durch diese Behandlungsmethode können viele Beschwerde- und Krankheitsbilder beeinflusst werden, die durch funktionelle Störungen im Körper verursacht worden sind.</p>
      <h4>Indikationen:</h4>
      <ul>
        <li class="hl">Wirbelsäulenbeschwerden</li>
        <li class="hl">Migräne</li>
        <li class="hl">Erkrankungen der Gelenke</li>
        <li class="hl">Neuralgien</li>
        <li class="hl">Durchblutungsstörungen</li>
        <li class="hl">u.v.m</li>
      </ul>
    </div>
    <svg class="swoosh" viewBox="0 0 195 72"><path d="M0 22Q100 4 195 12V72H0Z" fill="var(--mist)"/><path d="M0 22Q100 4 195 12" fill="none" stroke="var(--green)" stroke-width="2.5"/></svg>
  </article>

  <article class="panel panel--contact">
    <svg class="band" viewBox="0 0 195 50"><path d="M0 0H195V40Q90 30 0 34Z" fill="var(--blue)"/></svg>
    <p class="placeholder">Team/Praxisfoto hier?</p>
    <div class="brand" style="top:228px">
      <span class="brand-dot" style="width:14px;height:14px"></span>
      <p class="brand-name" style="font-size:9px">med. Massagepraxis<br>Lindqvorst</p>
    </div>
    <div class="contact">
      <p>Jonas Lindqvorst</p>
      <p>Lerchenweg 7 Haus 2</p>
      <p>2391 Waldhofen</p>
      <p>Tel: +43 660 555 01 27</p>
      <p>office@massagepraxis-lindqvorst.at</p>
      <p>www.massagepraxis-lindqvorst.at</p>
    </div>
    <svg class="swoosh" viewBox="0 0 195 72"><path d="M0 12Q100 4 195 20V72H0Z" fill="var(--mist)"/><path d="M0 12Q100 4 195 20" fill="none" stroke="var(--green)" stroke-width="2.5"/></svg>
    <p class="foot-note">Hausbesuche auf Anfrage</p>
  </article>

  <article class="panel panel--cover">
    <div class="brand" style="top:36px">
      <span class="brand-dot" style="width:22px;height:22px"></span>
      <p class="brand-name" style="font-size:13px">med. Massagepraxis<br>Lindqvorst</p>
    </div>
    <div class="grid" role="img" aria-label="Bildraster: neun Fotos von Massagegriffen an Schulter, Rücken, Händen und Knie">
      <div style="background:#d9b9a2"></div><div style="background:#c9c07a"></div><div style="background:#e2c6b3"></div>
      <div style="background:#d8cf8e"></div><div style="background:#e6c9b4"></div><div style="background:#c9c3cf"></div>
      <div style="background:#b9b7c6"></div><div style="background:#d6a98f"></div><div style="background:#e4cfc0"></div>
    </div>
    <p class="tagline">Schmerzfrei und vital leben</p>
    <svg class="swoosh" viewBox="0 0 195 72"><path d="M0 20Q100 2 195 8V72H0Z" fill="var(--mist)"/><path d="M0 20Q100 2 195 8" fill="none" stroke="var(--green)" stroke-width="2.5"/></svg>
    <p class="cover-note">EMS Training · Massage · Lymphdrainage ·<br>Akupunkt-Massage nach Hallbrecht</p>
  </article>
</section>

<!-- Inside of the folder -->
<section class="sheet sheet--inside">
  <article class="panel panel--ems">
    <div class="photo" style="top:34px;height:142px;background:linear-gradient(120deg,#c99a64,#e8d9c4 45%,#b88a55)" role="img" aria-label="Foto: Trainerin beim EMS-Ganzkörpertraining im Studio"></div>
    <svg class="band" viewBox="0 0 195 50"><path d="M0 0H195V30Q100 44 0 36Z" fill="var(--blue)"/></svg>
    <h2 class="band-title">EMS-Ganzkörpertraining</h2>
    <div class="copy" style="top:188px">
      <p><span class="hl">EMS (Elektro-Muskel-Stimulation)</span> ist eine neue Dimension des Ganzkörpertrainings.</p>
      <p>Schneller und intensiver als mit herkömmlichen Methoden, in weniger als 20 Minuten / Trainingseinheit und 1x pro Woche.</p>
      <p>Dadurch kann effektiv und effizienter trainiert werden, in allen Alters- und Leistungsstufen.</p>
      <ul>
        <li>Gesundheit bedeutet Lebensqualität</li>
        <li>für einen leistungsfähigen Körper</li>
        <li>Schlank &amp; Straff</li>
        <li>Fit im Sport</li>
      </ul>
    </div>
    <svg class="swoosh" viewBox="0 0 195 72"><path d="M0 16Q100 2 195 10V72H0Z" fill="var(--mist)"/><path d="M0 16Q100 2 195 10" fill="none" stroke="var(--green)" stroke-width="2.5"/></svg>
  </article>

  <article class="panel panel--massage" style="background:#f7f7f7">
    <div class="photo" style="top:34px;height:142px;background:linear-gradient(120deg,#d9c9b7,#efe4d9 50%,#a7c3dc)" role="img" aria-label="Foto: Therapeut massiert die Schulter einer Patientin"></div>
    <svg class="band" viewBox="0 0 195 50"><path d="M0 0H195V38Q100 46 0 36Z" fill="var(--blue)"/></svg>
    <h2 class="band-title" style="top:16px">Massage</h2>
    <div class="copy" style="top:188px">
      <p>Die <span class="hl">klassische Massage</span> dient vor allem zur Behandlung verspannter Muskulatur, oder zur Vorbeugung von Verspannungen.</p>
      <h4>Indikationen:</h4>
      <ul>
        <li>Bewegungseinschränkung durch Verspannungen am Rücken, Brust, Schulter, etc.</li>
        <li>Spannungskopfschmerzen</li>
        <li>Muskelschmerzen</li>
        <li>zur schnellen Regeneration nach dem Sport oder nach Verletzungen</li>
        <li>fördert die seelische und körperliche Ausgeglichenheit</li>
        <li>stabilisiert das Immunsystem</li>
        <li>verbessert den Lymphfluss</li>
        <li>wirkt sich positiv auf die Durchblutung der Haut und des Bindegewebes aus</li>
      </ul>
    </div>
    <svg class="swoosh" viewBox="0 0 195 72"><path d="M0 10Q100 2 195 16V72H0Z" fill="var(--mist)"/><path d="M0 10Q100 2 195 16" fill="none" stroke="var(--green)" stroke-width="2.5"/></svg>
    <p class="foot-note">Die Massagetherapie wird nach ärztlicher Verordnung durchgeführt.</p>
  </article>

  <article class="panel panel--lymph">
    <div class="photo" style="top:34px;height:142px;background:linear-gradient(120deg,#c79a7c,#e9cdb8 50%,#b98769)" role="img" aria-label="Foto: Hände bei der manuellen Lymphdrainage am Bein"></div>
    <svg class="band" viewBox="0 0 195 50"><path d="M0 0H195V40Q100 30 0 38Z" fill="var(--blue)"/></svg>
    <h2 class="band-title" style="top:16px">Lymphdrainage</h2>
    <div class="copy" style="top:192px">
      <p>Die sanften, schmerzfreien und langsam ausgeführten Griffe wirken:</p>
      <ul>
        <li>Entwässernd <span class="arrow">▸</span> entstauend</li>
        <li>Entspannend <span class="arrow">▸</span> entschlackend</li>
        <li>Beruhigend <span class="arrow">▸</span> entspannend</li>
        <li>stärken das Immunsystem</li>
        <li>bei Rheumatische Schwellungen</li>
      </ul>
      <h4>Indikationen:</h4>
      <ul>
        <li>nach Operationen</li>
        <li>nach Tumorbehandlungen</li>
        <li>nach Verletzungen</li>
        <li>nach Lymphknotenentfernungen</li>
        <li>nach Hämatomen (Bluterguß)</li>
        <li>hoher Muskeltonus</li>
      </ul>
    </div>
    <svg class="swoosh" viewBox="0 0 195 72"><path d="M0 16Q100 8 195 4V72H0Z" fill="var(--mist)"/><path d="M0 16Q100 8 195 4" fill="none" stroke="var(--green)" stroke-width="2.5"/></svg>
    <p class="foot-note">Über das Lymphsystem werden die meisten Abfallprodukte des Körpers abtransportiert.</p>
  </article>
</section>

</body>
</html>
```